TEK Logistics - Banner 2.5' x 8' for 20+ locations

Need a banner designed that will pop. This banner will be displayed at over 20 of our transportation facilities. Goal is for the banner to grab the attention of employees, contractors and clients and help reinforce our mission and core values. Designed needs to include TEK Logo, our core values and mission statement. Red and Black are the main company colors and we need to stay within that theme and color pallet. Attached is a previous version that was too basic and boring. Willing to consider a design that excludes the mission statement.

Gathering more feedback

```html
<!DOCTYPE html>
<html lang="en">
<head>
<meta charset="utf-8">
<title>TEK Logistics – Core Values Banner</title>
<link rel="stylesheet" href="https://fonts.googleapis.com/css2?family=Roboto:wght@500;700;900&display=swap">
<style>
  :root {
    --brand-red: #e0262b;
    --deep-red: #a01b20;
    --maroon: #5a0f12;
    --ink: #111011;
    --paper: #ffffff;
    --slate: #737273;
    --stage: #d9d9d9;
    --photo-site: #d89a86;
    --photo-office: #6d6864;
    --photo-yard: #5f8f88;
  }
  * { margin: 0; padding: 0; box-sizing: border-box; }
  html, body { width: 1200px; height: 600px; overflow: hidden; }
  body {
    background: var(--stage);
    display: flex; align-items: center; justify-content: center;
    font-family: "Roboto", Arial, sans-serif;
  }
  .banner { width: 1200px; height: 381px; display: block; }
  .headline { font-weight: 900; font-size: 88px; letter-spacing: 8px; }
  .value-line { font-weight: 700; font-size: 36px; letter-spacing: 3px; fill: var(--ink); }
  .value-line .accent { fill: var(--brand-red); }
  .value-line .accent-strong { fill: var(--deep-red); font-size: 44px; }
  .have-fun { font-weight: 700; font-size: 48px; letter-spacing: 3px; text-anchor: middle; }
  .mission-title { font-weight: 700; font-size: 42px; letter-spacing: 4px; }
  .mission-copy { font-weight: 700; font-size: 31px; fill: var(--paper); text-anchor: middle; }
  .brand-name { font-weight: 900; fill: var(--brand-red); text-anchor: middle; }
  .fill-red { fill: var(--brand-red); }
  .fill-white { fill: var(--paper); }
  .fill-ink { fill: var(--ink); }
</style>
</head>
<body>
<svg class="banner" viewBox="0 0 2420 768" xmlns="http://www.w3.org/2000/svg">
  <!-- base -->
  <rect width="2420" height="768" fill="var(--ink)"/>
  <polygon points="0,47 1495,47 1131,768 0,768" fill="var(--paper)"/>
  <polygon points="0,578 1245,578 1131,768 0,768" fill="var(--slate)"/>

  <!-- photo panels -->
  <polygon role="img" aria-label="Photo: engineers in hard hats and safety vests reviewing plans at a work site" points="1495,0 1915,0 1550,768 1131,768" fill="var(--photo-site)"/>
  <polygon role="img" aria-label="Photo: empty conference room with office chairs" points="1915,0 2375,0 1980,768 1550,768" fill="var(--photo-office)"/>
  <polygon role="img" aria-label="Photo: stacked shipping containers in a port yard" points="2375,0 2420,0 2420,768 1980,768" fill="var(--photo-yard)"/>

  <!-- top band -->
  <polygon points="0,0 1518,0 1495,47 0,47" fill="var(--maroon)"/>

  <!-- left chevron -->
  <polygon points="0,0 262,375 0,768" fill="var(--brand-red)"/>
  <polygon points="0,0 205,375 0,768" fill="var(--maroon)"/>
  <polygon points="0,0 145,375 0,768" fill="var(--ink)"/>

  <!-- header bar -->
  <path d="M395,47 L1475,47 L1420,162 L565,162 Q525,162 490,135 Z" class="fill-ink"/>
  <text class="headline" x="560" y="132" textLength="672" lengthAdjust="spacing"><tspan class="fill-red">CORE</tspan><tspan class="fill-white"> VALUES</tspan></text>

  <!-- brand -->
  <text class="brand-name" x="240" y="155" font-size="78">TEK</text>
  <text class="brand-name" x="240" y="192" font-size="30" letter-spacing="5">LOGISTICS</text>

  <!-- core values -->
  <text class="value-line" x="386" y="218" textLength="969" lengthAdjust="spacing">DO THE <tspan class="accent">RIGHT THINGS</tspan> FOR THE <tspan class="accent">RIGHT REASONS</tspan></text>
  <text class="value-line" x="386" y="279" textLength="754" lengthAdjust="spacing">PURSUE <tspan class="accent">GROWTH</tspan> AND <tspan class="accent">DEVELOPMENT</tspan></text>
  <text class="value-line" x="384" y="350" textLength="784" lengthAdjust="spacing">BUILD A <tspan class="accent">POSITIVE</tspan> <tspan class="accent-strong">TEAM</tspan> <tspan class="accent">ATMOSPHERE</tspan></text>
  <text class="value-line" x="388" y="418" textLength="670" lengthAdjust="spacing">DELIVER <tspan class="accent">WOW</tspan> THROUGH <tspan class="accent">SERVICE</tspan></text>
  <text class="value-line" x="388" y="486" textLength="487" lengthAdjust="spacing">DO EVERYTHING <tspan class="accent">SAFELY</tspan></text>
  <text class="have-fun fill-ink" x="1176" y="436">HAVE</text>
  <text class="have-fun fill-red" x="1176" y="486">FUN</text>

  <!-- mission -->
  <path d="M268,520 L1258,520 L1218,602 L352,602 Q322,602 300,580 Z" class="fill-ink"/>
  <text class="mission-title" x="418" y="575" textLength="500" lengthAdjust="spacing"><tspan class="fill-white">MISSION </tspan><tspan class="fill-red">STATEMENT</tspan></text>
  <text class="mission-copy" x="643" y="642">Provide the best customer experience while creating an</text>
  <text class="mission-copy" x="643" y="685">environment of growth and opportunity for our customers,</text>
  <text class="mission-copy" x="643" y="728">employees, and service providers</text>
</svg>
</body>
</html>
```